Lomi-Seret - Promote and Support a community

Design a website for Ethiopean Community. the design should be friendly, easy to navigate and maintain the look & feel of the Ethiopian culture. a proposed logo is attached but it can be change according to your recommendations. This is a project we are doing at a discount rate as it supports a weak community.
Please visit their current website http://www.lomi-seret.example.il/index.php?lang=en

Target Market(s)

Community members, potential doners

Industry/Entity Type

community

Number of Pages Required

1 page

Font styles to use
Sans Serif

Requirements
Must have
• easy to navigate friendly interface

```html
<!DOCTYPE html>
<html lang="en">
<head>
<meta charset="utf-8">
<title>Lomi-Seret – Promote and Support a Community</title>
<link rel="stylesheet" href="https://fonts.googleapis.com/css2?family=Maven+Pro:wght@500;700;800&family=Lato:ital,wght@0,400;0,700;0,900;1,400&display=swap">
<style>
  :root{
    --green:#1f8f62;
    --yellow:#d9b440;
    --maroon:#8b0000;
    --red:#d7141a;
    --ink:#1c1c1c;
    --grey-text:#8a8a8a;
    --light:#f2f2f2;
    --footer:#333333;
    --white:#ffffff;
  }
  *{box-sizing:border-box;margin:0;padding:0}
  html,body{width:1200px;height:4930px;overflow:hidden}
  body{position:relative;background:var(--white);font-family:'Lato',sans-serif;color:var(--ink)}
  section,header,footer{position:absolute;left:0;width:1200px}
  .abs{position:absolute}
  h1,h2,h3,.card-title{font-family:'Maven Pro',sans-serif;font-weight:700}
  .btn{position:absolute;display:flex;align-items:center;justify-content:center;font-family:'Lato',sans-serif;font-weight:900;font-size:9px;letter-spacing:1px;color:var(--white);text-transform:uppercase;border-radius:4px}
  .btn-maroon{background:var(--maroon)}
  .btn-green{background:var(--green)}
  .btn-red{background:var(--red)}
  .body-text{font-size:11.5px;line-height:21px}

  /* header */
  .site-header{top:0;height:96px;background:var(--white)}
  .brand{position:absolute;left:243px;top:16px;display:flex;align-items:center;gap:8px;font-family:'Lato',sans-serif;font-weight:900;font-size:15px;color:var(--maroon)}
  .brand-mark{width:60px;height:60px;border-radius:50%;border:3px solid var(--maroon)}
  .main-nav{position:absolute;right:243px;top:38px;display:flex;gap:20px;font-family:'Maven Pro',sans-serif;font-weight:700;font-size:10px;color:var(--ink)}
  .main-nav a{color:inherit;text-decoration:none;padding-bottom:6px}
  .main-nav a.current{color:var(--red);border-bottom:2px solid var(--red)}

  /* hero */
  .hero{top:96px;height:432px;background:linear-gradient(100deg,#4a5232 0%,#6b5a40 50%,#8a4a3a 100%)}
  .hero h1{position:absolute;left:241px;top:92px;width:470px;font-size:37px;line-height:46px;color:var(--white);font-weight:800}
  .hero p{position:absolute;left:241px;top:206px;width:385px;font-size:13.5px;line-height:27px;font-style:italic;color:var(--white)}
  .hero .btn{left:241px;top:272px;width:113px;height:38px}

  /* features */
  .features{top:528px;height:630px}
  .features-photo{position:absolute;left:0;top:0;width:1200px;height:444px;background:linear-gradient(180deg,#b9b9c2,#d6d6dd)}
  .card{position:absolute;top:347px;width:232px;height:283px;color:var(--white);text-align:center}
  .card svg{margin-top:30px}
  .card-title{font-size:21px;margin-top:6px}
  .card p{font-size:10px;line-height:20.5px;padding:0 24px;margin-top:10px;opacity:.92}
  .card .more{display:inline-block;margin-top:10px;font-size:9px;font-weight:900;letter-spacing:.8px;border-bottom:1px solid var(--white);padding-bottom:2px}
  .card-about{left:241px;background:var(--green)}
  .card-community{left:484px;background:var(--yellow)}
  .card-programs{left:727px;background:var(--maroon)}

  /* training */
  .training{top:1234px;height:274px}
  .training-panel{left:241px;top:0;width:324px;height:274px;background:var(--maroon)}
  .training-photo{left:301px;top:31px;width:206px;height:206px;border-radius:50%;background:#9a8068}
  .training-bar{left:588px;top:56px;width:36px;height:161px;background:var(--red)}
  .training h2{position:absolute;left:666px;top:20px;width:250px;font-size:17px;line-height:22px}
  .training p{position:absolute;left:666px;top:116px;width:280px;color:var(--grey-text)}
  .training .btn{left:666px;top:218px;width:120px;height:35px}

  /* health */
  .health{top:1546px;height:427px}
  .health-band{left:0;top:0;width:241px;height:427px;background:var(--green)}
  .health h2{position:absolute;left:270px;top:82px;width:340px;font-size:28px;line-height:37px}
  .health p{position:absolute;left:270px;top:168px;width:360px;font-size:10.5px;line-height:20px}
  .health-dot{left:272px;top:280px;width:56px;height:56px;border-radius:50%;background:var(--green)}
  .health-photo{left:656px;top:0;width:544px;height:427px;background:linear-gradient(160deg,#3d6a96,#8a7a6a)}

  /* support */
  .support{top:2010px;height:459px}
  .support-photo{left:0;top:0;width:469px;height:459px;background:linear-gradient(180deg,#c08c8e,#a87276)}
  .support-note{left:488px;top:0;width:249px;height:182px;background:var(--red);color:var(--white);padding:44px 20px 0}
  .support-note .eyebrow{font-size:11px;letter-spacing:2.5px;font-weight:900}
  .support-note p{font-size:10px;line-height:20px;font-weight:700;margin-top:18px}
  .support h2{position:absolute;left:507px;top:222px;font-size:28px}
  .support .copy{position:absolute;left:507px;top:270px;width:440px;font-size:10px;line-height:20.5px}
  .support .btn{left:507px;top:363px;width:120px;height:35px}

  /* partners */
  .partners{top:2515px;height:366px;text-align:center}
  .partners h2{position:absolute;left:0;width:1200px;top:32px;font-size:29px}
  .partners p{position:absolute;left:430px;width:340px;top:84px;font-size:10.5px;line-height:20px}
  .partner{position:absolute;background:#d7dde2;border-radius:4px}

  /* gallery */
  .gallery{top:2881px;height:641px;background:var(--yellow)}
  .gallery-item{position:absolute;width:221px;height:220px}
  .gallery .btn{left:528px;top:562px;width:142px;height:39px}

  /* newsletter */
  .newsletter{top:3522px;height:407px;background:var(--maroon);color:var(--white);text-align:center}
  .newsletter h2{position:absolute;left:0;width:1200px;top:74px;font-size:29px}
  .newsletter .rule{left:521px;top:120px;width:158px;height:4px;background:var(--white)}
  .newsletter .email{left:433px;top:170px;width:333px;height:29px;background:var(--white);color:#9a9a9a;font-size:10px;text-align:left;padding:9px 8px}
  .newsletter .btn{left:433px;top:212px;width:333px;height:31px;font-size:12px;letter-spacing:2px;border-radius:0}
  .newsletter p{position:absolute;left:490px;width:220px;top:266px;font-size:8.5px;line-height:17px}
  .social{position:absolute;top:325px;display:flex;gap:12px;left:570px}
  .social span{width:14px;height:14px;border-radius:50%;background:var(--white)}

  /* gift */
  .gift{top:3929px;height:496px;background:var(--light)}
  .gift-label{left:260px;top:86px;width:320px;height:60px;background:var(--green);color:var(--white);font-family:'Lato',sans-serif;font-weight:900;font-size:20px;letter-spacing:3.5px;line-height:26px;text-align:center;padding-top:5px}
  .gift .copy{position:absolute;left:270px;top:186px;width:300px;text-align:center;font-size:11px;line-height:23px;font-weight:700;color:#5a5a5a}
  .gift .btn{left:362px;top:334px;width:117px;height:36px}
  .gift-panel{left:599px;top:48px;width:358px;height:401px;background:var(--green)}
  .gift-photo{left:655px;top:137px;width:244px;height:244px;border-radius:50%;background:#a9b8c4}

  /* closing */
  .closing{top:4425px;height:429px;background:linear-gradient(180deg,#5d5a78,#4c4862);text-align:center;color:var(--white)}
  .closing .eyebrow{position:absolute;left:0;width:1200px;top:156px;font-weight:900;font-size:12px;letter-spacing:3.5px}
  .closing p{position:absolute;left:475px;width:250px;top:186px;font-size:11px;line-height:23px;opacity:.85}
  .closing .btn{left:541px;top:320px;width:118px;height:36px}

  .site-footer{top:4854px;height:76px;background:var(--footer);color:#d0d0d0;font-size:9px;text-align:center;line-height:76px}
</style>
</head>
<body>

<header class="site-header">
  <div class="brand"><span class="brand-mark"></span>Lomi-Seret</div>
  <nav class="main-nav">
    <a class="current" href="#">HOME</a>
    <a href="#">ABOUT</a>
    <a href="#">CONTACT</a>
    <a href="#">SUPPORT US</a>
  </nav>
</header>

<section class="hero" role="img" aria-label="Photo of a smiling young boy outdoors">
  <h1>Lomi-Seret lorem ipsum dolor</h1>
  <p>Lorem ipsum dolor sit amet, consectetur adipiscing elit. Pellentesque libero lorem, tempus quis vehicula vitae.</p>
  <span class="btn btn-maroon">Support us</span>
</section>

<section class="features">
  <div class="features-photo" role="img" aria-label="Photo of hands holding a red paper heart"></div>
  <article class="card card-about">
    <svg width="56" height="50" viewBox="0 0 56 50" fill="none" stroke="#fff" stroke-width="2"><circle cx="28" cy="9" r="6"/><path d="M18 24a10 7 0 0 1 20 0"/><circle cx="16" cy="31" r="6"/><path d="M6 46a10 7 0 0 1 20 0"/><circle cx="40" cy="31" r="6"/><path d="M30 46a10 7 0 0 1 20 0"/></svg>
    <div class="card-title">About</div>
    <p>Lorem ipsum dolor sit amet, consectetur adipiscing elit. Pellentesque libero lorem, tempus quis vehicula vitae, iaculis eget massa. Pellentesque habitant.</p>
    <span class="more">LEARN MORE</span>
  </article>
  <article class="card card-community">
    <svg width="56" height="50" viewBox="0 0 56 50" fill="none" stroke="#fff" stroke-width="2"><path d="M8 6l12 14M48 6L36 20M20 20l8 10 8-10M22 30h12v16H22z"/><path d="M28 4v10"/></svg>
    <div class="card-title">The Community</div>
    <p>Lorem ipsum dolor sit amet, consectetur adipiscing elit. Pellentesque libero lorem, tempus quis vehicula vitae, iaculis eget massa. Pellentesque habitant.</p>
    <span class="more">LEARN MORE</span>
  </article>
  <article class="card card-programs">
    <svg width="56" height="50" viewBox="0 0 56 50" fill="none" stroke="#fff" stroke-width="2"><circle cx="28" cy="11" r="8"/><path d="M14 46V32a14 10 0 0 1 28 0v14z"/><rect x="21" y="30" width="14" height="10"/></svg>
    <div class="card-title">Programs</div>
    <p>Lorem ipsum dolor sit amet, consectetur adipiscing elit. Pellentesque libero lorem, tempus quis vehicula vitae, iaculis eget massa. Pellentesque habitant.</p>
    <span class="more">LEARN MORE</span>
  </article>
</section>

<section class="training">
  <div class="abs training-panel"></div>
  <div class="abs training-photo" role="img" aria-label="Photo of workshop participants seated together"></div>
  <div class="abs training-bar"></div>
  <h2>Training on Cultural Competence for Israeli Healthcare Professionals</h2>
  <p class="body-text">Lorem ipsum dolor sit amet, consectetur adipiscing elit. Pellentesque libero lorem, tempus quis vehicula vitae, iaculis eget massa. Pellentesque habitant morbi tristique senectus.</p>
  <span class="btn btn-maroon">Learn more</span>
</section>

<section class="health">
  <div class="abs health-band"></div>
  <h2>Health &amp; the Ethiopian Israeli Community</h2>
  <p>Lorem ipsum dolor sit amet, consectetur adipiscing elit. Pellentesque libero lorem, tempus quis vehicula vitae, iaculis eget massa. Pellentesque habitant morbi tristique senectus et netus et malesuada fames ac turpis egestas.</p>
  <div class="abs health-dot"></div>
  <div class="abs health-photo" role="img" aria-label="Portrait photo of a woman wearing a white shawl"></div>
</section>

<section class="support">
  <div class="abs support-photo" role="img" aria-label="Photo of hands holding a red heart"></div>
  <div class="abs support-note">
    <div class="eyebrow">LOREM IPSUM</div>
    <p>Lorem ipsum dolor sit amet, consectetur adipiscing elit. Pellentesque libero lorem, tempus quis vehicula vitae.</p>
  </div>
  <h2>Support Us</h2>
  <p class="copy">Lorem ipsum dolor sit amet, consectetur adipiscing elit. Pellentesque libero lorem, tempus quis vehicula vitae, iaculis eget massa. Pellentesque habitant morbi tristique senectus et netus et malesuada fames ac turpis egestas. Cras laoreet congue commodo. Phasellus urna quam, tincidunt id arcu vitae.</p>
  <span class="btn btn-maroon">Learn more</span>
</section>

<section class="partners">
  <h2>Partners</h2>
  <p>Lorem ipsum dolor sit amet, consectetur adipiscing elit. Pellentesque libero lorem.</p>
  <span class="partner" style="left:306px;top:159px;width:52px;height:46px"></span>
  <span class="partner" style="left:446px;top:165px;width:126px;height:36px"></span>
  <span class="partner" style="left:648px;top:160px;width:74px;height:46px"></span>
  <span class="partner" style="left:840px;top:162px;width:62px;height:42px"></span>
  <span class="partner" style="left:402px;top:254px;width:34px;height:46px"></span>
  <span class="partner" style="left:536px;top:260px;width:128px;height:38px"></span>
  <span class="partner" style="left:716px;top:264px;width:126px;height:30px"></span>
</section>

<section class="gallery">
  <div class="gallery-item" style="left:241px;top:49px;background:linear-gradient(135deg,#7a6a55,#4b3e33)" role="img" aria-label="Photo of a community gathering"></div>
  <div class="gallery-item" style="left:490px;top:49px;background:linear-gradient(135deg,#c9c2b8,#6a5a50)" role="img" aria-label="Photo of a health workshop"></div>
  <div class="gallery-item" style="left:737px;top:49px;background:linear-gradient(135deg,#e0ddd8,#7b6558)" role="img" aria-label="Photo of a hand washing demonstration"></div>
  <div class="gallery-item" style="left:241px;top:296px;background:linear-gradient(135deg,#8a7a5a,#3e3530)" role="img" aria-label="Photo of children sharing a meal"></div>
  <div class="gallery-item" style="left:490px;top:296px;background:linear-gradient(135deg,#5aa090,#5a4338)" role="img" aria-label="Photo of a nutrition class"></div>
  <div class="gallery-item" style="left:737px;top:296px;background:linear-gradient(135deg,#cfd6e0,#5a5048)" role="img" aria-label="Photo of a health check appointment"></div>
  <span class="btn btn-green">Learn more</span>
</section>

<section class="newsletter">
  <h2>Newsletter</h2>
  <div class="abs rule"></div>
  <div class="abs email">Email</div>
  <span class="btn btn-red">Submit</span>
  <p>Lorem ipsum dolor sit amet, consectetur adipiscing elit. Pellentesque libero lorem.</p>
  <div class="social"><span></span><span></span><span></span></div>
</section>

<section class="gift">
  <div class="abs gift-label">Health is a gift to be preserved</div>
  <p class="copy">Duis aute irure dolor in reprehenderit in voluptate velit esse cillum dolore eu fugiat nulla pariatur. Excepteur sint occaecat cupidatat non proident, sunt in culpa qui officia deserunt mollit anim id est laborum.</p>
  <span class="btn btn-green">Support us</span>
  <div class="abs gift-panel"></div>
  <div class="abs gift-photo" role="img" aria-label="Photo of community members at a health event"></div>
</section>

<section class="closing" role="img" aria-label="Photo of hands holding a red heart over a wooden surface">
  <div class="eyebrow">WHAT YOU CAN DO</div>
  <p>Lorem ipsum dolor sit amet, consectetur adipiscing elit. Pellentesque libero lorem, tempus quis vehicula vitae, iaculis eget massa. Pellentesque habitant morbi tristique senectus et netus et malesuada.</p>
  <span class="btn btn-red">Learn more</span>
</section>

<footer class="site-footer">Lomi-Seret 2022. All rights reserved.</footer>

</body>
</html>
```